Nail salon window signage design

We need new signage to be designed for our existing nail salon. The sign will be a large sticker that will stick onto the glass window at the front.

Some of the services we provide are:
Manicures
Pedicures
Velora Gel Builder
Acrylic Nails
KVT
Brenlux
Gel Polish
You may wish to have our services listed on the sign but is not compulsory.

I have also attached our logo which can be used on the sign but is not compulsory.

I have also attached a photo of the front of our salon and the sign will be where I have outlined in yellow.

The size of the sign will be 119cm wide and 170cm high.

I am open to any nice classy design you can think of.

```html
<!DOCTYPE html>
<html lang="en">
<head>
<meta charset="utf-8">
<title>Aurelle Nails – Window Sign</title>
<link href="https://fonts.googleapis.com/css2?family=Montserrat:wght@500;700&display=swap" rel="stylesheet">
<style>
  :root {
    --burgundy: #8c1f35;
    --gold: #c9a66b;
    --ink: #555458;
    --paper: #ffffff;
    --backdrop: #ecebe8;
    --photo-light: #efe9e6;
    --photo-skin: #e3c2b2;
  }
  * { box-sizing: border-box; margin: 0; padding: 0; }
  html, body {
    width: 1200px; height: 990px; overflow: hidden;
    background: var(--backdrop);
    font-family: "Montserrat", Arial, sans-serif;
  }
  .sign {
    position: absolute; left: 275px; top: 30px;
    width: 650px; height: 930px;
    background: var(--paper);
    overflow: hidden;
    box-shadow: 0 6px 24px rgba(0,0,0,.12);
  }
  .sign-art { position: absolute; inset: 0; }
  .brand {
    position: absolute; left: 0; right: 0; top: 120px;
    text-align: center;
  }
  .brand-name {
    font-weight: 500; font-size: 64px; letter-spacing: 2px;
    color: var(--burgundy); line-height: 1;
  }
  .services-title {
    position: absolute; left: 50%; top: 300px; transform: translateX(-50%);
    background: var(--burgundy); color: var(--paper);
    font-weight: 700; font-size: 30px; letter-spacing: .5px;
    padding: 8px 22px; border-radius: 10px; white-space: nowrap;
  }
  .services-list {
    position: absolute; left: 0; right: 0; top: 380px;
    list-style: none; text-align: center;
    color: var(--ink); font-weight: 500; font-size: 27px; line-height: 40px;
  }
  .star { color: var(--gold); margin: 0 6px 0 14px; font-size: 24px; }
</style>
</head>
<body>
  <section class="sign">
    <svg class="sign-art" width="650" height="930" viewBox="0 0 650 930">
      <defs>
        <linearGradient id="photoTone" x1="0" y1="0" x2="1" y2="1">
          <stop offset="0" stop-color="var(--photo-light)"/>
          <stop offset=".55" stop-color="var(--photo-skin)"/>
          <stop offset="1" stop-color="var(--photo-light)"/>
        </linearGradient>
      </defs>
      <rect class="nail-photo" x="0" y="360" width="650" height="570" fill="url(#photoTone)"
            role="img" aria-label="Photo of two hands with long coffin-shaped French-tip nails on a light patterned backdrop"/>
      <ellipse class="gold-swoop" cx="325" cy="338" rx="322" ry="322" fill="var(--gold)"/>
      <ellipse class="panel-curve" cx="325" cy="320" rx="322" ry="322" fill="var(--paper)"/>
      <rect class="panel-top" x="0" y="0" width="650" height="330" fill="var(--paper)"/>
    </svg>

    <header class="brand">
      <h1 class="brand-name">Aurelle Nails</h1>
    </header>

    <h2 class="services-title">OUR SERVICES</h2>
    <ul class="services-list">
      <li><span class="star">★</span>MANICURES <span class="star">★</span>PEDICURES</li>
      <li><span class="star">★</span>VELORA GEL BUILDER</li>
      <li><span class="star">★</span>ACRYLIC NAILS</li>
      <li><span class="star">★</span>KVT <span class="star">★</span>BRENLUX</li>
      <li><span class="star">★</span>GEL POLISH</li>
    </ul>
  </section>
</body>
</html>
```